Beer bottle label / Tap badge

What: Graphics to be used on both a beer tap badge and a beer bottle label
Requirements:
• Represent a differentiated quality product
• Include brewery name and logo for brand recognition
• Include and represent the Name “Idle Tide”
• Include the beer style “American Cream Ale”
• A format that can be used both in a circular tap badge and a square / rectangular bottle label
At Drifting Reed Brewing Co. we design and brew quality beers across a range of styles. We use traditional ingredients and techniques to produce brews for you that are bursting with flavor and easy to drink. Our passion and commitment to excellence are captured in every bottle. Give them a try and see what we mean.
Idle Tide
American Cream Ale
An easy drinking session beer that won’t make you work to enjoy it. This is crafted to be smooth with a modicum of honey toasted oats and a yeast strain that leaves a fruity, very light, soft balanced palate. Perfectly hopped for a balanced experience this beer is made for you.
Updates
Thanks to everyone who submitted a design. My apologies for not providing any feedback over the past few days since we took a short break over Christmas. We've extended the deadline by a few days and we'll be in touch shortly.
Industry/Entity Type
Brewery
Requirements
Must have
- - Include brewery name and logo for brand recognition
- Include and represent the Name “Idle Tide”
- Include the beer style “American Cream Ale”
- include volume (330ml) and % alcohol (4.5% alcohol)
Nice to have
- Idle Tide is a very drinkable, smooth and easy beer that is perfect for a sunny lazy afternoon. We would like the graphic to represent the beer. So, perhaps a friendly (smiling) skeleton on a hammock or on the beach enjoying life .....

```html
<!DOCTYPE html>
<html lang="en">
<head>
<meta charset="utf-8">
<title>Idle Tide – American Cream Ale Label</title>
<link rel="stylesheet" href="https://fonts.googleapis.com/css2?family=Ultra&family=Arvo:wght@700&family=Fredoka:wght@600&display=swap">
<style>
  :root {
    --label-orange: #f99b66;
    --ink: #1a1a1a;
    --paper: #ffffff;
    --ribbon-red: #ef5a48;
    --ribbon-fold: #c9443a;
    --illustration-light: #f4efe9;
    --illustration-mid: #cfc6bd;
  }
  * { margin: 0; padding: 0; box-sizing: border-box; }
  html, body {
    width: 1053px;
    height: 1200px;
    overflow: hidden;
    background: var(--label-orange);
  }
  .label {
    position: relative;
    width: 1053px;
    height: 1200px;
    background: var(--label-orange);
    overflow: hidden;
  }
  .hammock-illustration {
    position: absolute;
    left: 90px;
    top: 90px;
    width: 873px;
    height: 580px;
    border-radius: 0 0 440px 440px / 0 0 200px 200px;
    background: linear-gradient(180deg, rgba(255,255,255,0) 0%, var(--illustration-light) 55%, var(--illustration-mid) 100%);
  }
  .brand-badge {
    position: absolute;
    left: 311px;
    top: 36px;
    width: 430px;
    height: 430px;
    border-radius: 50%;
    background: var(--paper);
    display: flex;
    align-items: center;
    justify-content: center;
    text-align: center;
  }
  .brand-name {
    font-family: "Arvo", serif;
    font-weight: 700;
    font-size: 46px;
    line-height: 1.1;
    color: var(--ink);
    width: 320px;
  }
  .beer-title { font-weight: normal; }
  .beer-name {
    position: absolute;
    left: 0;
    width: 100%;
    text-align: center;
    display: block;
  }
  .beer-name__first {
    top: 676px;
    font-family: "Fredoka", sans-serif;
    font-weight: 600;
    font-size: 150px;
    line-height: 1;
    letter-spacing: 28px;
    padding-left: 28px;
    color: var(--paper);
  }
  .beer-name__second {
    top: 830px;
    font-family: "Ultra", serif;
    font-size: 112px;
    line-height: 1;
    letter-spacing: 4px;
    color: var(--ink);
  }
  .style-ribbon {
    position: absolute;
    left: 206px;
    top: 960px;
    width: 640px;
    height: 230px;
  }
  .style-ribbon svg { position: absolute; left: 0; top: 0; }
  .style-ribbon__text {
    position: absolute;
    left: 0;
    top: 20px;
    width: 100%;
    text-align: center;
    font-family: "Arvo", serif;
    font-weight: 700;
    font-size: 50px;
    line-height: 1.05;
    color: var(--ink);
  }
  .strength {
    position: absolute;
    left: 0;
    top: 1102px;
    width: 100%;
    text-align: center;
    color: var(--ink);
    font-family: "Arvo", serif;
    font-weight: 700;
  }
  .strength__stars { font-size: 24px; letter-spacing: 8px; line-height: 1.2; }
  .strength__details {
    display: flex;
    align-items: center;
    justify-content: center;
    gap: 20px;
    font-size: 24px;
    margin-top: 8px;
  }
  .strength__rule { width: 70px; height: 2px; background: var(--ink); }
</style>
</head>
<body>
  <main class="label">
    <div class="hammock-illustration" role="img" aria-label="Illustration of a relaxed skeleton lying in a rope hammock"></div>

    <div class="brand-badge">
      <p class="brand-name">Drifting Reed Brewing Co.</p>
    </div>

    <h1 class="beer-title">
      <span class="beer-name beer-name__first">IDLE</span>
      <span class="beer-name beer-name__second">TIDE</span>
    </h1>

    <div class="style-ribbon">
      <svg width="640" height="230" viewBox="0 0 640 230" aria-hidden="true">
        <path d="M0 150 L80 150 L80 222 L0 222 L30 186 Z" fill="var(--ribbon-red)"/>
        <path d="M640 150 L560 150 L560 222 L640 222 L610 186 Z" fill="var(--ribbon-red)"/>
        <path d="M40 20 Q320 -4 600 20 L600 152 Q320 128 40 152 Z" fill="var(--paper)"/>
        <path d="M40 152 L80 190 L80 146 Z" fill="var(--ribbon-fold)"/>
        <path d="M600 152 L560 190 L560 146 Z" fill="var(--ribbon-fold)"/>
      </svg>
      <p class="style-ribbon__text">AMERICAN<br>CREAM ALE</p>
    </div>

    <div class="strength">
      <div class="strength__stars">★★★</div>
      <div class="strength__details">
        <span class="strength__rule"></span>
        <span>330ml · 4.5%</span>
        <span class="strength__rule"></span>
      </div>
    </div>
  </main>
</body>
</html>
```